KLV [Kindly Living Ventures]

We require a web design for a new line of products that we have created. The first of these is a product called B-GONE which is a natural product designed to repel animals such as Possums, snakes and Kangaroos in Australia and things like deer and Raccoons in the US.
Our Company and head office are in Sydney Australia and we have our own factories in Taiwan and China.
These items come in a few different forms such as Discs that can be thrown into a roof cavity, to a gell that comes in a PET container for use in the garden around plants and vegetables and an oil based spray that can be used on trucks of trees or plants and fences etc.
The final design should communicate an environmental and safe feeling for the user and also the animals it repels, but also make the user feel safe that they have B-goned the animals that were being a nuisance.

Target Market(s)

Home owners, gardeners, farmers

Industry/Entity Type

It Company

Requirements
Must have
• A green feeling that makes sure they understand that this product is a repellant and safe.
The Website must have the ability to grow outside the B-gone product line as new itmes are introduced such as Septic Bio products that break down waste and even make plants grow faster without chemicals.
Nice to have
• We already have a logo and trade mark for both KLV and B-gone which I will attach. The B-gone logo comes in different colours and animal images.
We were thinking of a name Fennel Wanderers as well but went with B-gone.
Should not have
• A green sell using the fonts etc included in the logos

```html
<!DOCTYPE html>
<html lang="en">
<head>
<meta charset="utf-8">
<title>KLV – Kindly Living Ventures</title>
<link href="https://fonts.googleapis.com/css2?family=Open+Sans:wght@400;600;700&display=swap" rel="stylesheet">
<style>
:root{
  --green:#8cc317;
  --green-dark:#79b00c;
  --green-light:#a8d84a;
  --blue:#1496dc;
  --blue-dark:#0a78c0;
  --heading-blue:#1a85cc;
  --text:#444;
  --text-dark:#333;
  --nav:#222;
  --footer:#1e1e1e;
  --panel:#eeeeee;
  --band:#f0f0f0;
  --body-font:Arial, Helvetica, sans-serif;
  --head-font:"Open Sans", Arial, sans-serif;
}
*{margin:0;padding:0;box-sizing:border-box}
html,body{width:1050px;height:1200px;overflow:hidden}
body{position:relative;background:#fafafa;font-family:var(--body-font);color:var(--text)}
.abs{position:absolute}

.site-header{left:0;top:0;width:1050px;height:120px;background:linear-gradient(#f2f2f2,#fdfdfd)}
.brand{left:39px;top:22px;display:flex;align-items:center;gap:12px}
.brand-mark{width:60px;height:60px;border-radius:50%;background:var(--green)}
.brand-name{font-family:var(--head-font);font-weight:700;font-size:54px;color:var(--green);letter-spacing:1px;line-height:1}
.call{left:768px;top:51px;display:flex;align-items:center;gap:14px;font-size:12px;font-weight:bold;color:var(--text-dark)}

.main-nav{left:25px;top:120px;width:998px;height:46px;background:var(--nav);border-bottom:3px solid #ddd}
.main-nav a{position:absolute;top:0;color:#fff;text-decoration:none;font-size:13px;font-weight:bold;line-height:46px;white-space:nowrap}
.main-nav a.current{left:42px;top:-7px;width:122px;height:50px;line-height:60px;text-align:center;background:linear-gradient(var(--blue),var(--blue-dark));border-radius:4px 4px 0 0}
.nav-sep{position:absolute;top:5px;width:1px;height:36px;background:#555}

.slider{left:39px;top:177px;width:970px;height:325px;background:#333;padding:2px}
.slide-photo{width:100%;height:100%;background:linear-gradient(135deg,#3f6a2a,#6c8f45 35%,#9aa3a7 50%,#6b5038 70%,#2f3a22)}
.arrow{top:143px}
.arrow.prev{left:20px}
.arrow.next{left:920px}
.caption{left:2px;bottom:2px;width:966px;height:42px;background:rgba(20,20,20,.75);color:var(--green-light);font-size:15px;text-align:right;padding:10px 32px 0 0}

.animal{top:527px;width:154px;height:176px;border-radius:10px;border:2px solid #b7dc68;background:linear-gradient(#a2d146,var(--green) 45%,var(--green-dark));text-align:center}
.animal .num{position:absolute;left:43px;top:-11px;width:66px;height:30px;border-radius:14px;background:linear-gradient(#5cc4f5,var(--blue-dark));color:#fff;font-family:var(--head-font);font-size:18px;font-weight:600;line-height:28px;box-shadow:0 2px 3px rgba(0,0,0,.25)}
.animal .name{position:absolute;left:0;top:27px;width:100%;font-family:var(--head-font);font-weight:600;font-size:18px;color:#fff}
.animal .figure{position:absolute;left:22px;top:82px;width:106px;height:70px;border-radius:50%;background:rgba(255,255,255,.85)}

.welcome{left:42px;top:725px;width:640px}
.welcome h1{font-family:var(--head-font);font-weight:600;font-size:18px;color:var(--heading-blue);margin-bottom:14px}
.welcome h2{font-size:12px;font-weight:bold;color:var(--text-dark);margin-bottom:11px}
.welcome p{font-size:12px;line-height:22px;color:var(--text);white-space:nowrap}
.btn-green{background:var(--green);color:#fff;font-family:var(--head-font);font-weight:600;font-size:13px;text-align:center;line-height:24px}
.welcome-more{left:577px;top:908px;width:85px;height:24px}

.promo{left:695px;top:723px;width:312px;height:142px;border:3px solid var(--green);background:var(--panel)}
.promo-mark{left:12px;top:12px;width:52px;height:52px;border-radius:50%;background:#222}
.promo-brand{left:72px;top:26px;font-family:var(--head-font);font-weight:700;font-size:18px;color:var(--green)}
.promo h3{left:144px;top:18px;font-family:var(--head-font);font-weight:600;font-size:23px;color:var(--text-dark);line-height:1.05}
.promo h3 small{font-size:17px}
.promo p{left:18px;top:78px;width:280px;font-size:11px;line-height:15px;color:var(--text)}
.btn-dark{background:linear-gradient(#444,#1d1d1d);color:#fff;font-size:11px;text-align:center;line-height:20px}
.buy{left:141px;top:112px;width:68px;height:20px}
.view{left:222px;top:112px;width:68px;height:20px}

.newsletter{left:696px;top:876px;width:310px;height:68px;background:var(--panel)}
.envelope{left:10px;top:14px;width:52px;height:40px;background:linear-gradient(#fff,#cfd8e0);border-radius:3px;transform:rotate(-10deg)}
.newsletter h4{left:82px;top:7px;font-family:var(--head-font);font-weight:600;font-size:14px;color:var(--heading-blue)}
.mail-field{left:82px;top:33px;width:154px;height:25px;background:var(--green);color:#fff;font-size:10px;line-height:25px;padding-left:9px}
.subscribe{left:239px;top:33px;width:54px;height:25px;background:linear-gradient(#44b8f0,var(--blue-dark));color:#fff;font-size:11px;line-height:25px;text-align:center}

.info-band{left:0;top:955px;width:1050px;height:161px;background:var(--band)}
.band-title{font-family:var(--head-font);font-weight:600;font-size:16px;color:#555;top:7px}
.band-rule{top:33px;height:2px;background:#ccc}
.pager{top:8px;font-size:18px;line-height:18px;color:#666;font-weight:bold;letter-spacing:4px}
.divider{left:431px;top:12px;width:1px;height:142px;background:#ccc}
.entry-title{font-size:10px;font-weight:bold;color:var(--text-dark)}
.entry-text{font-size:10px;line-height:16px;color:#555}
.read-more{font-size:10px;font-weight:bold;color:var(--text-dark);text-decoration:underline}
.avatar{left:43px;top:43px;width:58px;height:54px;background:linear-gradient(#ddd,#999);border:1px solid #ccc}
.who{left:38px;top:104px;width:70px;text-align:center;font-size:10px;line-height:16px;color:#555}
.product-photo{left:455px;top:46px;width:232px;height:104px;border:2px solid #ccc;background:linear-gradient(135deg,#6b3a2c,#8a5a44 50%,#4b2a20)}

.site-footer{left:0;top:1116px;width:1050px;height:84px;background:var(--footer);color:#fff;font-size:11px}
.footer-nav{left:43px;top:25px}
.footer-nav span{margin:0 9px;color:#aaa}
.copyright{left:43px;top:55px}
.connect{left:822px;top:23px}
.socials{left:824px;top:48px;display:flex;gap:14px}
.socials i{display:block;width:26px;height:22px;border-radius:3px}
</style>
</head>
<body>

<header class="site-header abs">
  <div class="brand abs"><span class="brand-mark"></span><span class="brand-name">KLV</span></div>
  <div class="call abs">
    <svg width="20" height="16" viewBox="0 0 20 16"><path d="M1 5 Q10 -1 19 5 L17 8 L14 6 L14 4 Q10 2 6 4 L6 6 L3 8 Z" fill="#333"/><rect x="4" y="8" width="12" height="7" rx="1" fill="#333"/></svg>
    CALL US : 555 210 4837
  </div>
</header>

<nav class="main-nav abs">
  <a class="current" href="#">HOME</a>
  <a href="#" style="left:195px">WHAT WE DO</a>
  <span class="nav-sep" style="left:319px"></span>
  <a href="#" style="left:355px">OUR PRODUCTS</a>
  <span class="nav-sep" style="left:497px"></span>
  <a href="#" style="left:536px">FAQ</a>
  <span class="nav-sep" style="left:601px"></span>
  <a href="#" style="left:635px">CONTACT US</a>
</nav>

<section class="slider abs">
  <div class="slide-photo" role="img" aria-label="Photo of a silver station wagon in a forest with a stag crossing beside it"></div>
  <svg class="arrow prev abs" width="36" height="40" viewBox="0 0 36 40"><path d="M28 2 L8 20 L28 38 L34 34 L18 20 L34 6 Z" fill="#eee"/></svg>
  <svg class="arrow next abs" width="36" height="40" viewBox="0 0 36 40"><path d="M8 2 L28 20 L8 38 L2 34 L18 20 L2 6 Z" fill="#eee"/></svg>
  <div class="caption abs">Cicero are also reproduced in their exact original form, accompanied by English</div>
</section>

<div class="animal abs" style="left:40px"><span class="num">01</span><span class="name">Possums</span><div class="figure" role="img" aria-label="White possum silhouette"></div></div>
<div class="animal abs" style="left:203px"><span class="num">02</span><span class="name">Kangaroo</span><div class="figure" role="img" aria-label="White kangaroo silhouette"></div></div>
<div class="animal abs" style="left:366px"><span class="num">03</span><span class="name">Snakes</span><div class="figure" role="img" aria-label="White snake silhouette"></div></div>
<div class="animal abs" style="left:528px"><span class="num">04</span><span class="name">Rodents</span><div class="figure" role="img" aria-label="White mouse silhouette"></div></div>
<div class="animal abs" style="left:690px"><span class="num">05</span><span class="name">Deer</span><div class="figure" role="img" aria-label="White deer silhouette"></div></div>
<div class="animal abs" style="left:853px"><span class="num">06</span><span class="name">Raccoons</span><div class="figure" role="img" aria-label="White raccoon silhouette"></div></div>

<section class="welcome abs">
  <h1>Welcome To Our Site</h1>
  <h2>It is a long established fact that a reader will be distracted</h2>
  <p>The readable content of a page when looking at its layout. The point of using Lorem Ipsum is that it has a more-or-less<br>normal distribution of letters, as opposed to using 'Content here, content here', making it look like readable English.<br>Many desktop publishing packages and web page editors now use Lorem Ipsum as their default model text, and a<br>search for 'lorem ipsum' will uncover many web sites still in their infancy. Various versions have evolved over the years,<br>sometimes by accident, sometimes on purpose (injected humour and the like).</p>
</section>
<div class="btn-green welcome-more abs">View more</div>

<aside class="promo abs">
  <div class="promo-mark abs"></div>
  <div class="promo-brand abs">B-gone</div>
  <h3 class="abs">B-gone <small>from<br>your home</small></h3>
  <p class="abs">Integer ornare orci quis nibh bibendum tristique Morbi aliquet laoreet elit, et tincidunt dolor laoreet varius.</p>
  <div class="btn-dark buy abs">Buy this</div>
  <div class="btn-dark view abs">View more</div>
</aside>

<aside class="newsletter abs">
  <div class="envelope abs" role="img" aria-label="Envelope with letter illustration"></div>
  <h4 class="abs">News Letter</h4>
  <div class="mail-field abs">Enter your mail ID</div>
  <div class="subscribe abs">Subscribe</div>
</aside>

<section class="info-band abs">
  <h3 class="band-title abs" style="left:39px">Testimonials</h3>
  <span class="pager abs" style="left:382px">‹›</span>
  <div class="band-rule abs" style="left:39px;width:372px"></div>
  <div class="avatar abs" role="img" aria-label="Customer portrait placeholder"></div>
  <div class="who abs">Mo Jarvis<br>Oct 15, 2011</div>
  <div class="entry-title abs" style="left:116px;top:45px">It is a long established fact that a reader will be distracted</div>
  <p class="entry-text abs" style="left:116px;top:66px;width:290px">The readable content of a page when looking at its layout. The point of using Lorem Ipsum is that it has a more-or-less normal distribution of letters, as opposed to using 'Content here, content here', making it look like readable English.</p>
  <span class="read-more abs" style="left:347px;top:135px">Read more</span>

  <div class="divider abs"></div>

  <h3 class="band-title abs" style="left:450px">Featured Products</h3>
  <span class="pager abs" style="left:793px">‹›</span>
  <div class="band-rule abs" style="left:445px;width:566px"></div>
  <div class="product-photo abs" role="img" aria-label="Photo of a brown rat with product badge"></div>
  <div class="entry-title abs" style="left:717px;top:45px">It is a long established fact that a reader will be distracted</div>
  <p class="entry-text abs" style="left:717px;top:66px;width:290px">The readable content of a page when looking at its layout. The point of using Lorem Ipsum is that it has a more-or-less normal distribution of letters, as opposed to using 'Content here, content here', making it look like readable English.</p>
  <span class="read-more abs" style="left:948px;top:135px">Read more</span>
</section>

<footer class="site-footer abs">
  <div class="footer-nav abs">Home<span>|</span>What we do<span>|</span>Our Products<span>|</span>FAQ<span>|</span>Contact Us<span>|</span>Sitemap</div>
  <div class="copyright abs">Copyright © 2011 www.klv-ventures.com All rights reserved</div>
  <div class="connect abs">Connect with us :</div>
  <div class="socials abs">
    <i style="background:#3b5b9a"></i>
    <i style="background:#4fb9de"></i>
    <i style="background:#f08a1e"></i>
    <i style="background:#2a7fb8"></i>
    <i style="background:#3a6fa8"></i>
  </div>
</footer>

</body>
</html>
```